Junior Recital Advertisement (Saxophone)

Hey guys! I'm in need of some help in preparation for my saxophone recital. I'm currently a student at the University of Carrowfield and I am doing a recital with a brass/saxophone influence. (Alto/Trumpet Quintet, solo piece, Sextet for alto and brass quintet). My title of the recital will be "Vinculum Aureum: a collaboration of saxophone and brass" or something of that nature. I know I like the idea of Vinculum Aureum (which is latin for bridge, being saxophone is a bridge instrument)
I would like to see a design that is relevant to the title and "celebrates" the idea of saxophone and brass together. Please be as creative as you would like. Do not let my directions restrict you but aid you
*INFO*
Dalton Velisek Junior Recital
Oswin Marlow Hall
8pm
April 19th, 2012
Target Market(s)
College Students; to be around around the school of music
Industry/Entity Type
University

```html
<!DOCTYPE html>
<html lang="en">
<head>
<meta charset="utf-8">
<title>Dalton Velisek Recital — Vinculum Aureum</title>
<link rel="stylesheet" href="https://fonts.googleapis.com/css2?family=Cutive+Mono&family=Questrial&display=swap">
<style>
  :root {
    --paper: #ffffff;
    --ink: #1a1a1a;
    --accent-red: #a3161a;
    --brass-light: #f1dc9a;
    --brass-mid: #d8b356;
    --silver: #d3d6d9;
    --key-blue: #8fa9d4;
  }
  html, body {
    margin: 0;
    padding: 0;
    overflow: hidden;
    background: var(--paper);
  }
  .poster {
    position: relative;
    width: 900px;
    height: 1200px;
    background: var(--paper);
    color: var(--ink);
    overflow: hidden;
    font-family: "Cutive Mono", "Courier New", monospace;
  }
  .mono { font-family: "Cutive Mono", "Courier New", monospace; }
  .sans { font-family: "Questrial", "Helvetica", sans-serif; }

  .performer-title {
    position: absolute;
    top: 10px;
    left: 0;
    width: 900px;
    text-align: center;
    font-size: 50px;
    letter-spacing: 5px;
    margin: 0;
    font-weight: 400;
    white-space: nowrap;
    line-height: 1;
  }
  .instrument-photo {
    position: absolute;
    left: 470px;
    top: 65px;
    width: 320px;
    height: 930px;
    background: linear-gradient(160deg, var(--silver) 0%, var(--key-blue) 25%, var(--brass-mid) 60%, var(--brass-light) 100%);
  }
  .date-block span { position: absolute; white-space: nowrap; line-height: 1; }
  .month { left: 54px; top: 656px; font-size: 60px; letter-spacing: 1px; }
  .day { left: 252px; top: 604px; font-size: 112px; }
  .day-suffix { left: 376px; top: 656px; font-size: 58px; }
  .year { left: 54px; top: 716px; font-size: 62px; letter-spacing: 4px; }
  .hour { left: 302px; top: 690px; font-size: 128px; }
  .meridiem { left: 382px; top: 712px; font-size: 50px; }

  .venue {
    position: absolute;
    left: 40px;
    top: 1008px;
    font-size: 58px;
    letter-spacing: 5px;
    margin: 0;
    font-weight: 400;
    white-space: nowrap;
    line-height: 1;
  }
  .program-title {
    position: absolute;
    left: 36px;
    top: 1060px;
    font-size: 86px;
    margin: 0;
    font-weight: 400;
    white-space: nowrap;
    line-height: 1;
  }
  .program-title .colon { color: var(--accent-red); }
  .program-subtitle {
    position: absolute;
    left: 38px;
    top: 1158px;
    font-size: 36px;
    margin: 0;
    white-space: nowrap;
    line-height: 1;
  }
</style>
</head>
<body>
<main class="poster">
  <h1 class="performer-title mono">DALTON VELISEK RECITAL</h1>

  <div class="instrument-photo" role="img" aria-label="Photograph of a brass alto saxophone, angled diagonally, with blue and green accents traced along its keys"></div>

  <div class="date-block">
    <span class="month mono">April</span>
    <span class="day sans">19</span>
    <span class="day-suffix mono">th</span>
    <span class="year sans">2012</span>
    <span class="hour sans">8</span>
    <span class="meridiem mono">pm</span>
  </div>

  <h2 class="venue mono">OSWIN MARLOW HALL</h2>
  <h2 class="program-title mono">VINCULUM AUREUM<span class="colon">:</span></h2>
  <p class="program-subtitle mono">a collaboration of saxophone and brass</p>
</main>
</body>
</html>
```